Business Card Design

Name of company: Brisk Property Maintenance.
We are a new start up business.
The company is involved in general property maintenance around residential properties and high rise apartment buildings.
We carry out all types of property maintenance such as:
*Handyman work
*Plumbing
*Painting
*Electrical
*Window cleaning
*Gardens / Landscaping

Target Market(s)

*Real Estate Agents
*Body corporate managers
*Private apartment owners

Industry/Entity Type

Property Maintenance

Requirements
Must have
• Name: Dean Malloy
Address: PO Box 3862
Carrow Hill Crossing
NSW 2089
Phone: 0431 962 305
Email: dean@briskpropertymaintenance
Website: www.briskpropertymaintenance.example.au
Nice to have
• We don't have any corporate logo so you can design what you think is appropriate

```html
<!DOCTYPE html>
<html lang="en">
<head>
<meta charset="utf-8">
<title>Brisk Property Maintenance – Business Card</title>
<link rel="stylesheet" href="https://fonts.googleapis.com/css2?family=Open+Sans:ital,wght@0,300;0,400;0,700;1,700&display=swap">
<style>
  :root {
    --backdrop: #e6e6e6;
    --card: #ffffff;
    --red-light: #c01a22;
    --red-mid: #8a1216;
    --red-dark: #3f0709;
    --edge-shadow: #2a2a2a;
    --text-light: #ffffff;
    --text-dark: #1c1c1c;
    --mark: #b3161d;
  }
  * { box-sizing: border-box; margin: 0; padding: 0; }
  html, body {
    width: 1200px; height: 1200px; overflow: hidden;
    background: var(--backdrop);
  }
  .stage {
    width: 1200px; height: 1200px;
    display: flex; align-items: center; justify-content: center;
  }
  .business-card {
    position: relative;
    width: 1000px; height: 580px;
    background: var(--card);
    box-shadow: 0 12px 30px rgba(0,0,0,0.18);
    font-family: "Open Sans", Arial, sans-serif;
  }
  .red-panel { position: absolute; inset: 0; }
  .contact-block {
    position: absolute;
    top: 64px; right: 30px;
    text-align: right;
    color: var(--text-light);
  }
  .holder-name {
    font-size: 42px; font-weight: 700; font-style: italic;
    line-height: 1.1;
    margin-right: 38px;
    margin-bottom: 14px;
  }
  .contact-line {
    display: flex; justify-content: flex-end; align-items: center;
    font-size: 24px; font-weight: 300; line-height: 1.5;
    white-space: nowrap;
  }
  .contact-line .icon {
    width: 24px; height: 24px; margin-left: 14px; flex: none;
  }
  .contact-line.no-icon { padding-right: 38px; }
  .brand {
    position: absolute;
    left: 38px; top: 410px;
    display: flex; align-items: center; gap: 14px;
  }
  .brand-dot {
    width: 58px; height: 58px; border-radius: 50%;
    background: var(--mark); flex: none;
  }
  .brand-name {
    font-size: 25px; font-weight: 700; line-height: 1.15;
    color: var(--text-dark);
  }
</style>
</head>
<body>
<main class="stage">
  <article class="business-card">
    <svg class="red-panel" width="1000" height="580" viewBox="0 0 1000 580" aria-hidden="true">
      <defs>
        <linearGradient id="panelFill" x1="0" y1="0" x2="1" y2="1">
          <stop offset="0" stop-color="var(--red-light)"/>
          <stop offset="0.55" stop-color="var(--red-mid)"/>
          <stop offset="1" stop-color="var(--red-dark)"/>
        </linearGradient>
      </defs>
      <path d="M 244 552 C 396 420 416 150 336 28" fill="none" stroke="var(--edge-shadow)" stroke-width="9" stroke-linecap="round"/>
      <path d="M 340 30 H 970 V 550 H 250 C 400 420 420 150 340 30 Z" fill="url(#panelFill)"/>
    </svg>

    <section class="contact-block">
      <h1 class="holder-name">Dean Malloy</h1>
      <p class="contact-line">0431 962 305
        <svg class="icon" viewBox="0 0 24 24" aria-hidden="true"><path d="M6.6 10.8a15 15 0 0 0 6.6 6.6l2.2-2.2a1 1 0 0 1 1-.25 11.4 11.4 0 0 0 3.6.57 1 1 0 0 1 1 1V20a1 1 0 0 1-1 1A17 17 0 0 1 3 4a1 1 0 0 1 1-1h3.5a1 1 0 0 1 1 1c0 1.250.2 2.450.57 3.570a1 1 0 0 1-.25 1z" fill="#fff"/></svg>
      </p>
      <p class="contact-line">dean@briskpropertymaintenance.example.au
        <svg class="icon" viewBox="0 0 24 24" aria-hidden="true"><rect x="3" y="5" width="18" height="14" rx="2" fill="#fff"/><path d="M4 6l8 7 8-7" fill="none" stroke="#8a1216" stroke-width="1.8"/></svg>
      </p>
      <p class="contact-line">www.briskpropertymaintenance.example.au
        <svg class="icon" viewBox="0 0 24 24" aria-hidden="true"><g fill="none" stroke="#fff" stroke-width="1.8"><circle cx="12" cy="12" r="9"/><ellipse cx="12" cy="12" rx="4" ry="9"/><path d="M3 12h18M5 7h14M5 17h14"/></g></svg>
      </p>
      <p class="contact-line">PO Box 3862
        <svg class="icon" viewBox="0 0 24 24" aria-hidden="true"><path d="M12 2a7 7 0 0 0-7 7c0 5 7 13 7 13s7-8 7-13a7 7 0 0 0-7-7zm0 9.5A2.5 2.5 0 1 1 12 6.5a2.5 2.5 0 0 1 0 5z" fill="#fff"/></svg>
      </p>
      <p class="contact-line no-icon">Carrow Hill Crossing</p>
      <p class="contact-line no-icon">NSW 2089</p>
    </section>

    <div class="brand">
      <span class="brand-dot" aria-hidden="true"></span>
      <p class="brand-name">Brisk Property<br>Maintenance</p>
    </div>
  </article>
</main>
</body>
</html>
```